First Reponders Promotion poster/flyer

Our Yoga studio is introducing an ongoing promotion for all First Responders, Police/Nurse/Paramedic/Firefighters/Doctors
$22pw for Unlimited access to our Inner city Studio which will become a sanctuary for the people who look after us. Tag line: You look after us, let us look after you. The benefits of yoga, reduce stress, clear mind, healthy body. Feel free to use other assets, and be as creative as you like I have just put images and designs as a guide.

Target Market(s)

Emergency Services Tasmania

Industry/Entity Type

Emergency Services

Requirements
Must have
• Stillwave Logo/Address 41 Marlow St/ website www.stillwavestudio.com.a/ sign up online and just bring in current work Id at checkin/$22pw Unlimited classes/Australian market so can't look like usa or any other countries
Nice to have
• words , inner city Sanctuary
Should not have
• Foreign Country images

```html
<!DOCTYPE html>
<html lang="en">
<head>
<meta charset="utf-8">
<title>Stillwave – First Responders Promotion</title>
<link href="https://fonts.googleapis.com/css2?family=Poppins:wght@400;500;600;700;800&family=Oswald:wght@500&display=swap" rel="stylesheet">
<style>
  :root {
    --yellow: #f3c21b;
    --charcoal: #2b2b2c;
    --ink: #1b1b1b;
    --white: #ffffff;
    --backdrop: #ecebe8;
    --photo-top: #2a3550;
    --photo-mid: #3d4e7a;
    --photo-warm: #c0582e;
  }
  * { box-sizing: border-box; margin: 0; padding: 0; }
  html, body { width: 1200px; height: 800px; overflow: hidden; }
  body { background: var(--backdrop); font-family: "Poppins", sans-serif; position: relative; }

  .flyer {
    position: absolute; left: 330px; top: 20px;
    width: 598px; height: 843px;
    transform: scale(0.9016); transform-origin: 0 0;
    background: var(--charcoal); overflow: hidden;
    box-shadow: 0 6px 18px rgba(0,0,0,.25);
  }
  .abs { position: absolute; }

  .hero-photo {
    left: 0; top: 0; width: 598px; height: 317px;
    background: linear-gradient(100deg, #6b5a3a 0%, var(--photo-warm) 25%, var(--photo-top) 45%, var(--photo-mid) 70%, #5f86c2 100%);
  }
  .hero-photo::after {
    content: ""; position: absolute; inset: 0;
    background: linear-gradient(180deg, rgba(20,24,40,.55) 0%, rgba(20,24,40,0) 45%);
  }

  .yellow-band { left: 0; top: 317px; width: 598px; height: 170px; background: var(--yellow); }

  .role-circle {
    width: 116px; height: 116px; border-radius: 50%;
    border: 4px solid var(--white); top: 249px;
    background: linear-gradient(160deg, #3a4a6e, #1e2536);
  }
  .role-circle.fire { left: 227px; background: linear-gradient(160deg, #6a5a40, #2e2a24); }
  .role-circle.medic { left: 352px; }
  .role-circle.police { left: 476px; background: linear-gradient(160deg, #5a6a3a, #25305a); }

  .headline {
    left: 28px; top: 346px; width: 290px;
    font-weight: 800; font-size: 31px; line-height: 43px; color: var(--ink); letter-spacing: .2px;
  }

  .roles { top: 386px; list-style: none; font-size: 15.5px; color: var(--ink); line-height: 28px; }
  .roles.left { left: 326px; }
  .roles.right { left: 462px; }
  .roles li { display: flex; align-items: center; gap: 7px; }
  .roles svg { width: 20px; height: 18px; flex: none; }

  .left-photo {
    left: 90px; top: 495px; width: 210px; height: 250px;
    background: radial-gradient(ellipse at 55% 40%, rgba(120,120,120,.35), rgba(43,43,44,0) 70%);
  }

  .info { left: 28px; width: 290px; font-size: 13.5px; line-height: 18px; color: var(--white); }
  .info .label { color: var(--yellow); font-weight: 600; }
  .info.why { top: 512px; }
  .info.faq { top: 597px; }
  .info.signup { top: 684px; }
  .info .url { color: var(--yellow); font-weight: 600; font-size: 15.5px; margin-top: 6px; }
  .divider { left: 29px; width: 37px; height: 9px; border-top: 3px solid var(--yellow); border-bottom: 3px solid var(--yellow); }
  .divider.one { top: 576px; }
  .divider.two { top: 665px; }

  .logo-panel { left: 0; top: 757px; width: 305px; height: 86px; }
  .brand {
    left: 0; top: 757px; width: 290px; height: 86px;
    display: flex; align-items: center; justify-content: center; gap: 10px;
  }
  .brand-dot { width: 14px; height: 14px; border-radius: 50%; background: var(--ink); }
  .brand-name { font-weight: 600; font-size: 24px; color: var(--ink); }
  .bottom-strip { left: 300px; top: 820px; width: 298px; height: 23px; background: var(--yellow); }

  .date-banner {
    left: 330px; top: 513px; width: 242px; height: 26px;
    background: var(--yellow); clip-path: polygon(2% 0, 100% 0, 98% 100%, 0 100%);
    text-align: center; font-weight: 600; font-size: 17px; line-height: 26px; color: var(--ink);
  }
  .venue { left: 330px; top: 548px; width: 242px; text-align: center; font-weight: 600; font-size: 15.5px; color: var(--white); }
  .venue-note { left: 330px; top: 582px; width: 242px; text-align: center; font-size: 13.5px; line-height: 18px; color: var(--white); }
  .venue-url { left: 325px; top: 624px; width: 252px; text-align: center; font-weight: 600; font-size: 15.5px; color: var(--yellow); }

  .promo-box { left: 341px; top: 660px; width: 230px; height: 141px; border: 1.5px solid var(--yellow); border-radius: 6px; overflow: hidden; }
  .promo-head { left: 343px; top: 660px; width: 226px; height: 30px; background: var(--yellow); border-radius: 0 0 10px 10px; text-align: center; font-weight: 600; font-size: 17px; line-height: 30px; color: var(--ink); }
  .promo-title { left: 341px; top: 703px; width: 230px; text-align: center; font-weight: 600; font-size: 20px; color: var(--yellow); }
  .promo-note { left: 350px; top: 741px; width: 125px; font-size: 8.5px; line-height: 13px; color: var(--white); }
  .promo-price { left: 477px; top: 732px; font-family: "Oswald", sans-serif; font-weight: 500; font-size: 40px; line-height: 48px; color: var(--yellow); }
  .promo-price small { font-size: 26px; }
</style>
</head>
<body>
<main class="flyer">
  <div class="abs hero-photo" role="img" aria-label="Group photo of Australian first responders: firefighter, SES volunteer, paramedic, police officer and nurse against a night city skyline"></div>
  <div class="abs yellow-band"></div>
  <div class="abs role-circle fire" role="img" aria-label="Firefighter in breathing gear"></div>
  <div class="abs role-circle medic" role="img" aria-label="Paramedic uniform seen from behind"></div>
  <div class="abs role-circle police" role="img" aria-label="Police officer in high-visibility vest"></div>

  <h1 class="abs headline">YOU LOOK<br>AFTER US, LET US<br>LOOK AFTER YOU.</h1>

  <ul class="abs roles left">
    <li><svg viewBox="0 0 20 18"><rect x="2" y="5" width="16" height="11" rx="2" fill="#1b1b1b"/><rect x="7" y="2" width="6" height="4" fill="none" stroke="#1b1b1b" stroke-width="1.6"/><path d="M10 8v6M7 11h6" stroke="#f3c21b" stroke-width="1.6"/></svg>Paramedic</li>
    <li><svg viewBox="0 0 20 18"><rect x="1" y="5" width="13" height="9" fill="#1b1b1b"/><path d="M14 8h3l2 3v3h-5z" fill="#1b1b1b"/><circle cx="5" cy="15" r="2" fill="#1b1b1b"/><circle cx="15" cy="15" r="2" fill="#1b1b1b"/></svg>Ambulance</li>
    <li><svg viewBox="0 0 20 18"><circle cx="10" cy="5" r="3.5" fill="#1b1b1b"/><path d="M4 17c0-5 3-7 6-7s6 2 6 7z" fill="#1b1b1b"/></svg>Nurse</li>
  </ul>
  <ul class="abs roles right">
    <li><svg viewBox="0 0 20 18"><path d="M5 15V9a5 5 0 0 1 10 0v6z" fill="#1b1b1b"/><rect x="3" y="15" width="14" height="2" fill="#1b1b1b"/><path d="M10 0v2M2 4l2 1M18 4l-2 1" stroke="#1b1b1b" stroke-width="1.5"/></svg>Police</li>
    <li><svg viewBox="0 0 20 18"><path d="M3 9a7 7 0 0 1 14 0h2v2H1V9z" fill="#1b1b1b"/><circle cx="10" cy="14" r="3" fill="#1b1b1b"/></svg>Firefighters</li>
    <li><svg viewBox="0 0 20 18"><path d="M5 1v6a4 4 0 0 0 8 0V1" fill="none" stroke="#1b1b1b" stroke-width="1.6"/><path d="M9 11v3a3 3 0 0 0 6 0v-3" fill="none" stroke="#1b1b1b" stroke-width="1.6"/><circle cx="15" cy="9" r="2" fill="#1b1b1b"/></svg>SES/Doctors</li>
  </ul>

  <div class="abs left-photo" role="img" aria-label="Faded portrait of a doctor with a stethoscope"></div>

  <section class="abs info why">
    <p class="label">Why:</p>
    <p>Yoga helps Stress, Mental<br>Health, Fitness</p>
  </section>
  <div class="abs divider one"></div>
  <section class="abs info faq">
    <p class="label">Questions you might have:</p>
    <p>Is there any contract?</p>
    <p>No, only email 2 weeks prior to cancel</p>
  </section>
  <div class="abs divider two"></div>
  <section class="abs info signup">
    <p class="label">Sign Up Online</p>
    <p>just bring in current work ID at checkin</p>
    <p class="url">www.stillwavestudio.com.au</p>
  </section>

  <svg class="abs logo-panel" viewBox="0 0 305 86" aria-hidden="true"><polygon points="0,0 272,0 305,86 0,86" fill="#ffffff"/></svg>
  <div class="abs brand">
    <span class="brand-dot"></span>
    <p class="brand-name">Stillwave</p>
  </div>
  <div class="abs bottom-strip"></div>

  <p class="abs date-banner">From July 1 2022</p>
  <p class="abs venue">at 41 Marlow St, Hobart</p>
  <p class="abs venue-note">Just sign up on Website and bring<br>in you Current ID for verification</p>
  <p class="abs venue-url">www.stillwavestudio.com.au</p>

  <div class="abs promo-box"></div>
  <p class="abs promo-head">PROMO:</p>
  <p class="abs promo-title">FIRST RESPONDERS</p>
  <p class="abs promo-note">Unlimited access to our<br>classes in our beautiful<br>inner-city Studio Sanctuary</p>
  <p class="abs promo-price">$22<small>PW</small></p>
</main>
</body>
</html>
```